Education provider needs a landing page for its brand

We need a landing page for an advertising campaign that we are currently running on hireloop.com.au.
We're Tallowby Institute. We offer Australian online qualifications (courses) that help people get jobs with the right knowledge.
We'd like a landing page that shows our quirky, fun style that breaks away from traditional, conservative education advertising. The final landing page needs to be a strong converter for leads as it can take up to 90 days for someone to decide to study a course.
Check out our website. www.tallowby.edu.au

We also like the attached landing pages by Zivo and Pell Academy.

Target Market(s)

25-45 yr olds who have recently searched for a course to study on Hireloop.

Font styles to use
Sans Serif

Colors
3276b5
85acd3
ecf5f6
87d0c7

Requirements
Must have
• - Simple and uncluttered
- Logo
- Video - https://vidhost.example/v/Qw8mXz2LkTa
- 3 x dot points about why Tallowby is your best educator partner
- It needs a lead form to capture user's details so we can nurture them in an email campaign. This will be a 'Learn More' button that allows them to add their name and email address and they will be sent information.
- 'Enrol Now' button
Nice to have
• - Simple list of courses that we offer

```html
<!DOCTYPE html>
<html lang="en">
<head>
<meta charset="utf-8">
<title>Tallowby Institute — Enrol</title>
<link rel="stylesheet" href="https://fonts.googleapis.com/css2?family=Montserrat:wght@400;500;600;700&family=Signika:wght@600&display=swap">
<style>
:root{
  --navy:#1b3d66;
  --blue:#3276b5;
  --sky:#85acd3;
  --teal:#27d3c4;
  --white:#ffffff;
  --ink:#1d1d1f;
  --line:#c9ccd2;
  --mist:#ecf5f6;
}
*{box-sizing:border-box;margin:0;padding:0}
html,body{width:1200px;height:845px;overflow:hidden}
body{font-family:'Montserrat',sans-serif;color:var(--white);position:relative;background:var(--white)}
.hero{position:absolute;left:0;top:0;width:1200px;height:676px;overflow:hidden}
.hero-photo{position:absolute;inset:0;background:linear-gradient(100deg,#1a3a70 0%,#2b5ca3 45%,#234d92 70%,#1b3b74 100%)}
.hero-photo::after{content:"";position:absolute;inset:0;background:radial-gradient(ellipse at 45% 35%,rgba(90,140,200,.35),transparent 60%)}
.brand{position:absolute;left:144px;top:14px;display:flex;flex-direction:column;align-items:center;width:148px}
.brand-square{width:48px;height:48px;background:#cfd3d8;margin-bottom:22px}
.brand-name{font-weight:500;font-size:24px;letter-spacing:1px;color:var(--white);text-align:center;line-height:1.1}
.brand-name span{display:block;font-size:16px;letter-spacing:1.5px;margin-top:3px}
.nav a{position:absolute;top:39px;color:var(--white);text-decoration:none;font-size:13px;font-weight:500;padding:0 2px 6px;border-bottom:2px solid transparent;white-space:nowrap}
.nav a.active{border-bottom-color:var(--teal)}
.phone{position:absolute;left:905px;top:34px;display:flex;align-items:center;gap:7px;font-weight:700;font-size:19px;color:var(--white);white-space:nowrap}
.headline{position:absolute;left:144px;top:278px;font-family:'Signika',sans-serif;font-weight:600;font-size:38px;line-height:50px;letter-spacing:.3px}
.points{position:absolute;left:144px;top:394px;list-style:none}
.points li{display:flex;align-items:center;gap:17px;font-size:16px;font-weight:500;height:33.5px}
.cta-outline{position:absolute;left:145px;top:533px;width:183px;height:51px;border:2px solid var(--teal);border-radius:26px;display:flex;align-items:center;justify-content:center;font-weight:700;font-size:16px;color:var(--white)}
.play{position:absolute;left:584px;top:613px}
.enrol-card{position:absolute;left:746px;top:191px;width:310px;height:407px;background:var(--white);padding:0 27px}
.enrol-card h2{font-family:'Signika',sans-serif;font-weight:600;color:var(--navy);font-size:30px;text-align:center;margin-top:30px;letter-spacing:.5px}
.field{display:block;width:257px;height:44px;border:1px solid var(--line);margin-top:10px;padding:0 18px;font-size:12px;font-weight:500;color:var(--ink);line-height:44px}
.field:first-of-type{margin-top:22px}
.field.message{height:76px;line-height:1;padding-top:16px}
.enrol-btn{display:flex;margin:18px auto 0;width:162px;height:45px;border-radius:23px;background:var(--teal);color:var(--white);font-weight:700;font-size:15px;align-items:center;justify-content:center}
.courses{position:absolute;left:0;top:676px;width:1200px;height:75px;background:var(--white)}
.arrow{position:absolute;top:15px;width:44px;height:44px;border:1px solid #d6d8dc;border-radius:50%;display:flex;align-items:center;justify-content:center}
.arrow.prev{left:24px}.arrow.next{left:1132px}
.course{position:absolute;top:5px;height:65px;display:flex;align-items:center;gap:16px;color:var(--ink);font-weight:600;font-size:16.5px;line-height:21px;letter-spacing:.3px;white-space:nowrap}
.course.divided{border-left:1px solid #e4e6ea}
.footer{position:absolute;left:0;top:751px;width:1200px;height:94px;background:var(--sky)}
.social{position:absolute;left:144px;top:38px;display:flex;gap:20px}
.social i{display:block;width:20px;height:20px;border-radius:50%;background:var(--white)}
.legal{position:absolute;right:145px;top:39px;font-size:14px;color:var(--white)}
.legal span{margin:0 7px}
</style>
</head>
<body>
<section class="hero">
  <div class="hero-photo" role="img" aria-label="Blue-toned photo of an excited student celebrating in a bright office"></div>

  <div class="brand">
    <div class="brand-square"></div>
    <div class="brand-name">TALLOWBY<span>INSTITUTE</span></div>
  </div>

  <nav class="nav">
    <a href="#" class="active" style="left:551px">COURSES</a>
    <a href="#" style="left:641px">ABOUT</a>
    <a href="#" style="left:714px">MORE INFO</a>
    <a href="#" style="left:815px">CONTACT</a>
  </nav>
  <div class="phone">
    <svg width="18" height="18" viewBox="0 0 24 24"><path fill="#fff" d="M6.6 10.8a15.1 15.1 0 0 0 6.6 6.6l2.2-2.2a1 1 0 0 1 1-.25 11.4 11.4 0 0 0 3.6.57 1 1 0 0 1 1 1V20a1 1 0 0 1-1 1A17 17 0 0 1 3 4a1 1 0 0 1 1-1h3.5a1 1 0 0 1 1 1c0 1.250.2 2.450.57 3.57a1 1 0 0 1-.25 1z"/></svg>
    1300 555 014
  </div>

  <h1 class="headline">WHY TALLOWBY IS YOUR<br>BEST EDUCATOR PARTNER?</h1>
  <ul class="points">
    <li><svg width="17" height="17" viewBox="0 0 20 20"><circle cx="10" cy="10" r="10" fill="#27d3c4"/><path d="M5.5 10.3l3 3 6-6" stroke="#fff" stroke-width="2.4" fill="none"/></svg>Get the skills that employers really want.</li>
    <li><svg width="17" height="17" viewBox="0 0 20 20"><circle cx="10" cy="10" r="10" fill="#27d3c4"/><path d="M5.5 10.3l3 3 6-6" stroke="#fff" stroke-width="2.4" fill="none"/></svg>Absolute flexibility.Your way, your terms.</li>
    <li><svg width="17" height="17" viewBox="0 0 20 20"><circle cx="10" cy="10" r="10" fill="#27d3c4"/><path d="M5.5 10.3l3 3 6-6" stroke="#fff" stroke-width="2.4" fill="none"/></svg>Unrivalled support.Delivered with care.</li>
  </ul>
  <a class="cta-outline">LEARN MORE</a>

  <svg class="play" width="32" height="32" viewBox="0 0 32 32" aria-label="Play video"><circle cx="16" cy="16" r="15.5" fill="#fff"/><path d="M12.5 9.5v13l10-6.5z" fill="#111"/></svg>

  <form class="enrol-card">
    <h2>ENROLL HERE</h2>
    <span class="field">Enter Name</span>
    <span class="field">Enter Email</span>
    <span class="field">City</span>
    <span class="field message">Message</span>
    <span class="enrol-btn">ENROLL NOW</span>
  </form>
</section>

<section class="courses">
  <div class="arrow prev"><svg width="12" height="20" viewBox="0 0 12 20"><path d="M10 2L2 10l8 8" stroke="#aaa" stroke-width="1.6" fill="none"/></svg></div>

  <div class="course" style="left:96px">
    <svg width="36" height="46" viewBox="0 0 36 46" fill="none" stroke="#444" stroke-width="1.2"><rect x="1" y="1" width="34" height="44"/><rect x="5" y="5" width="26" height="8"/><rect x="6" y="18" width="10" height="9"/><rect x="20" y="18" width="10" height="9"/><rect x="6" y="31" width="10" height="9"/><rect x="20" y="31" width="10" height="9" stroke="#3276b5"/><path d="M11 20v5M8.5 22.5h5M8.5 33.5l5 4M13.5 33.5l-5 4M22 22.5h6M23 34h5M23 37h5"/></svg>
    ACCOUNTING</div>

  <div class="course divided" style="left:282px;padding-left:30px">
    <svg width="40" height="36" viewBox="0 0 40 36" fill="none" stroke="#444" stroke-width="1.2"><path d="M2 8l32-7v27L2 35z"/><path d="M34 4h4v30H2"/><path d="M8 29h8" stroke="#3276b5"/></svg>
    FINANCIAL<br>PLANNING</div>

  <div class="course divided" style="left:495px;padding-left:20px">
    <svg width="42" height="40" viewBox="0 0 42 40" fill="none" stroke="#444" stroke-width="1.2"><rect x="2" y="3" width="12" height="6" stroke="#f0a040"/><rect x="28" y="3" width="12" height="6" stroke="#3276b5"/><path d="M2 9h12v24H2zM28 9h12v24H28zM14 16h14v10H14z"/><rect x="3" y="33" width="10" height="5"/><rect x="29" y="33" width="10" height="5"/></svg>
    BUSINESS<br>MANAGEMENT</div>

  <div class="course divided" style="left:722px;padding-left:30px">
    <svg width="40" height="40" viewBox="0 0 40 40" fill="none" stroke="#444" stroke-width="1.2"><path d="M2 20l18-10 18 10v19H2z"/><path d="M20 2v8M17 4h6"/><path d="M9 25v14M13 25v14M17 25v14M21 25v14M25 25v14M29 25v14M33 25v14"/><path d="M4 30h3" stroke="#27d3c4"/></svg>
    LOGISTICS</div>

  <div class="course divided" style="left:920px;padding-left:27px">
    <svg width="44" height="36" viewBox="0 0 44 36" fill="none" stroke="#444" stroke-width="1.2"><path d="M2 12h8l14-10v32L10 24H2z"/><path d="M6 12v12" stroke="#e05a8a"/><path d="M29 12a7 7 0 0 1 0 12M33 8a12 12 0 0 1 0 20M37 4a17 17 0 0 1 0 28"/></svg>
    MARKETING</div>

  <div class="arrow next"><svg width="12" height="20" viewBox="0 0 12 20"><path d="M2 2l8 8-8 8" stroke="#aaa" stroke-width="1.6" fill="none"/></svg></div>
</section>

<footer class="footer">
  <div class="social" aria-label="Social links"><i></i><i></i><i></i><i></i></div>
  <p class="legal">© Tallowby.All rights reserved<span>|</span>Privacy Policy<span>|</span>Terms and Use</p>
</footer>
</body>
</html>
```